Redesign 2016 Digital Marketing Website and Convert to Wordpress

Technology needed to integrate:

- redesign and convert to wordpress
- gravity forms
- malware and hacker defense / honeypot (must be very secure from hackers)
- I want gravity forms to be a flow that asks many questions with icons and progress bar.
- 1 home page design
- 1 blog design
- 1 design for internal page content
- 1 multi step gravity form
I want to focus on SMB's. We are a marketing agency thats been around since 2016.

Site is: bluemoth.agency

I am looking to redesign the homepage, blog page and services page. The services page will be a template for all inner pages of the site. All content needs to be moved into the new design.

I want to get ride of the weird video.

I need you to install gravity forms pro model so we can pass utms.

I need the gravity form to be a multi step form with icons.

All "contact us" or "get a free assesments" call to actions will go to this form only.

step 1:
what is your website

step 2:
what industry are you in
- option
- Home Services
- Legal
- Ecommerce
- Lead Gen

No matter which one they select its going to produce a differnt calculator for them.

Law:
How many leads did you get last month
how much is each ase worth on average
How much revenue do you want to make

Home servicse:
How many bookings did you get last month
How much is each service worht on average
How much revenue do you wangt to make

Ecommerce:
What is your average order value
How muny purchases did you have last month
How much revenue did you drive
How much revenue do you want to drive

For lead gen:
How many leads did you get lawt month
How much revenue did they generate

Step 3:
What is your current advertising budget

step 4:
Do you have a CRM and if so what is it

Step 5:
What is your personal informagtion
name
email
phone

Let me know if this is enough to get you going

Target Market(s)

Small and medium sized law firms, ecommerce, home services and lead gen customers.

Industry/Entity Type

We are a digital marketing agency

Coding

Coded - Design and coding required

Number of Pages Required

5+ page

Font styles to use
Other font styles liked:
• Use whats on the current site and improve upon it

Requirements
Must have
• Must be very secure, developed into a wordpress website. using gravity forms. remove my photo and my staffs photo, depersonalize it so it doesnt mention me or tom fenley. Use the same color scheme. I am looking to redesign the homepage, blog page and services page. The services page will be a template for all inner pages of the site. All content needs to be moved into the new design. I want to get ride of the weird video. I need you to install gravity forms pro model so we can pass utms. I need the gravity form to be a multi step form with icons. All "contact us" or "get a free assesments" call to actions will go to this form only. step 1: what is your website step 2: what industry are you in - option - Home Services - Legal - Ecommerce - Lead Gen No matter which one they select its going to produce a differnt calculator for them. Law: How many leads did you get last month how much is each ase worth on average How much revenue do you want to make Home servicse: How many bookings did you get last month How much is each service worht on average How much revenue do you wangt to make Ecommerce: What is your average order value How muny purchases did you have last month How much revenue did you drive How much revenue do you want to drive For lead gen: How many leads did you get lawt month How much revenue did they generate How much revenue do you want to make Step 3: What is your current advertising budget step 4: Do you have a CRM and if so what is it Step 5: What is your personal informagtion name email phone Let me know if this is enough to get you going
Should not have
• SHOULD NOT BE SLOPPY, I AM LOOKING FOR ATTENTION TO DETAIL.

```html
<!DOCTYPE html>
<html lang="en">
<head>
<meta charset="utf-8">
<title>Blue Moth – Contact Page Options</title>
<link href="https://fonts.googleapis.com/css2?family=Montserrat:wght@400;500;600;700;800&family=Roboto+Condensed:wght@400;700&display=swap" rel="stylesheet">
<style>
:root{
  --board:#bdbdbd;
  --ink:#2b2b2b;
  --ink-soft:#555;
  --brand:#6e1116;
  --brand-deep:#560b10;
  --brand-light:#8b2a2e;
  --white:#fff;
  --line:#dcdcdc;
  --muted-btn:#9c9a9a;
  --map:#e6e6e6;
}
*{box-sizing:border-box;margin:0;padding:0}
html,body{width:1200px;height:1071px;overflow:hidden}
body{background:var(--board);font-family:"Montserrat",sans-serif;color:var(--ink);position:relative}
.board-title{position:absolute;top:48px;width:515px;text-align:center;font-weight:800;font-size:37px;letter-spacing:.5px;color:#2e2e2e}
.board-title--one{left:72px}
.board-title--two{left:619px}

.page{position:absolute;top:125px;width:515px;height:914px;background:var(--white);overflow:hidden}
.page--one{left:72px}
.page--two{left:619px}
.abs{position:absolute}

/* header */
.site-header{left:0;top:0;width:515px;height:29px;background:var(--white)}
.brand{display:flex;align-items:center;gap:5px}
.brand__mark{width:22px;height:22px;border-radius:50%;background:var(--brand);flex:none}
.brand__name{font-weight:400;font-size:10px;letter-spacing:1.2px;color:var(--ink-soft)}
.site-header .brand{position:absolute;left:41px;top:3.5px}
.nav{left:0;top:0;height:29px;width:515px;list-style:none}
.nav li{position:absolute;top:11px;font-size:6.2px;font-weight:500;letter-spacing:.2px;color:var(--ink)}
.nav li.is-active::after{content:"";position:absolute;left:50%;top:10px;width:18px;margin-left:-9px;height:1px;background:var(--brand)}
.header-cta{left:415px;top:0;width:100px;height:29px;background:var(--brand);clip-path:polygon(5px 0,100% 0,100% 100%,0 100%);font-family:"Roboto Condensed",sans-serif;color:var(--white);padding:7px 0 0 19px}
.header-cta strong{display:block;font-size:6px;font-weight:700;letter-spacing:.1px}
.header-cta span{display:block;font-size:5px;margin-top:1.5px}

/* hero */
.hero{left:0;top:29px;width:515px;height:180px}
.hero--mesh{background:radial-gradient(ellipse at 70% 85%,#4a4a4c 0%,#262628 35%,#151516 70%),#151516}
.hero--desk{background:linear-gradient(100deg,#9ea4ab 0%,#6d747c 28%,#3b3d42 55%,#1d1b1d 80%,#191718 100%)}
.hero__kicker{color:var(--white);font-weight:400}
.hero__title{color:var(--white);font-weight:500;letter-spacing:.3px}
.page--one .hero__copy{left:0;top:59px;width:515px;text-align:center}
.page--one .hero__kicker{font-size:11.5px}
.page--one .hero__title{font-size:19px;margin-top:1px}
.page--two .hero__copy{left:45px;top:70px}
.page--two .hero__kicker{font-size:9.5px}
.page--two .hero__title{font-size:20px;margin-top:0}

/* section heading */
.section-title{font-size:15px;font-weight:600;letter-spacing:.2px;color:var(--ink)}
.section-title em{font-style:normal;color:var(--brand)}
.rule{height:1px;background:var(--line);width:72px}
.rule::before{content:"";display:block;width:28px;height:2px;margin-top:-.5px;background:var(--brand)}
.lead{font-size:7px;line-height:8.8px;color:var(--ink)}

/* contact list (option 1) */
.contact-list{left:56px;top:320px;list-style:none}
.contact-list li{position:absolute;left:0;display:flex;align-items:center;gap:6px;font-size:7px;line-height:10.5px;font-weight:500;width:200px}
.icon-disc{width:20px;height:20px;border-radius:50%;background:var(--brand);display:flex;align-items:center;justify-content:center;flex:none}
.icon-disc svg{width:10px;height:10px;fill:var(--white)}

/* message form */
.msg-form{border-radius:4px;background:linear-gradient(110deg,var(--brand-deep) 0%,var(--brand) 55%,var(--brand-light) 100%)}
.msg-form__title{position:absolute;font-size:10.3px;font-weight:600;color:var(--white);letter-spacing:.2px}
.field{position:absolute;background:var(--white);height:18px;font-size:5.2px;color:var(--ink);padding:6.5px 0 0 7px}
.field--area{padding-top:6px}
.btn-outline{position:absolute;height:20px;border:1.2px solid var(--white);border-radius:10px;color:var(--white);font-size:5.8px;font-weight:700;display:flex;align-items:center;justify-content:center;letter-spacing:.2px}

/* info cards (option 2) */
.info-card{top:343px;width:122px;height:81px;border:1px solid #d6d6d6;border-radius:3px;background:linear-gradient(#fff 60%,#f4f4f4);box-shadow:0 1px 3px rgba(0,0,0,.12);text-align:center;padding-top:11px}
.info-card .icon-disc{margin:0 auto}
.info-card__label{font-size:7.4px;color:var(--ink-soft);margin-top:4px}
.info-card__value{font-size:7.4px;font-weight:600;line-height:9.8px;color:var(--ink);margin-top:1px}

/* map */
.map{left:0;top:455px;width:515px;height:212px;background:linear-gradient(180deg,#ececec,#e1e1e1)}
.map__pin{position:absolute;left:261px;top:542px;width:18px;height:18px}

/* footer */
.footer-top .brand{position:absolute;left:59px;top:683px}
.footer-top .brand__mark{width:23px;height:23px}
.footer-top .brand__name{font-size:11px}
.pill{position:absolute;top:682px;width:93px;height:21px;border-radius:11px;color:var(--white);font-size:5.6px;font-weight:700;display:flex;align-items:center;justify-content:center;letter-spacing:.2px}
.pill--muted{left:261px;background:var(--muted-btn)}
.pill--brand{left:360px;background:var(--brand)}
.footer-rule{position:absolute;left:0;width:515px;height:1px;background:var(--line)}
.footer-col{position:absolute;top:729px}
.footer-col h4{font-size:7px;font-weight:700;letter-spacing:.2px;border-left:1.5px solid var(--brand);padding-left:4px;line-height:8px}
.footer-col ul{list-style:none;margin:5px 0 0 6px}
.footer-col li{font-size:5.8px;line-height:9.9px;color:var(--ink-soft)}
.copyright{position:absolute;left:0;top:894px;width:515px;text-align:center;font-size:5.3px;color:var(--ink-soft)}
</style>
</head>
<body>

<svg width="0" height="0" style="position:absolute" aria-hidden="true">
  <symbol id="i-pin" viewBox="0 0 24 24"><path d="M12 1.5a7.5 7.5 0 0 0-7.5 7.5c0 5.6 7.5 13.5 7.5 13.5s7.5-7.9 7.5-13.5A7.5 7.5 0 0 0 12 1.5zm0 10.4a2.9 2.9 0 1 1 0-5.8 2.9 2.9 0 0 1 0 5.8z"/></symbol>
  <symbol id="i-phone" viewBox="0 0 24 24"><path d="M6.6 2.5l3 3.4c.5.6.5 1.4 0 2l-1.6 1.8c1.1 2.4 3 4.3 5.4 5.4l1.8-1.6c.6-.5 1.4-.5 2 0l3.4 3c.6.5.6 1.4.1 2l-1.7 2c-.6.7-1.6 1-2.5.7C9.6 19.2 4.8 14.4 2.8 7.5c-.3-.9 0-1.9.7-2.5l2-1.7c.6-.5 1.5-.4 2 .1z"/></symbol>
  <symbol id="i-mail" viewBox="0 0 24 24"><path d="M2 5h20v14H2zm2 2v.4l8 6 8-6V7zm0 2.9V17h16V9.9l-8 6z"/></symbol>
</svg>

<h1 class="board-title board-title--one">CONTACT OPTION 1</h1>
<h1 class="board-title board-title--two">CONTACT OPTION 2</h1>

<!-- ===== Option 1 ===== -->
<section class="page page--one">
  <header class="site-header abs">
    <div class="brand"><span class="brand__mark"></span><span class="brand__name">BLUE MOTH</span></div>
    <ul class="nav abs">
      <li style="left:164px">ABOUT</li>
      <li style="left:204px">INDUSTRIES</li>
      <li style="left:260px">SERVICES</li>
      <li style="left:310px">BLOG</li>
      <li class="is-active" style="left:345px">CONTACT US</li>
    </ul>
    <div class="header-cta abs"><strong>GET A FREE CONSULTATION</strong><span>OR CALL US (480) 555-0142</span></div>
  </header>

  <div class="hero hero--mesh abs" role="img" aria-label="Dark abstract background with a flowing particle mesh wave"></div>
  <div class="hero__copy abs">
    <p class="hero__kicker">GET IN TOUCH</p>
    <h2 class="hero__title">CONTACT BLUE MOTH</h2>
  </div>

  <h3 class="section-title abs" style="left:56px;top:259px">GET IN TOUCH <em>WITH US</em></h3>
  <div class="rule abs" style="left:56px;top:281px;width:100px"></div>
  <p class="lead abs" style="left:57px;top:292px;width:185px">Are you ready to kick your business into high gear? Our strategists are standing by. Contact us now!</p>

  <ul class="contact-list abs">
    <li style="top:0"><span class="icon-disc"><svg><use href="#i-pin"/></svg></span><span>Address: 18 W. Harbor Ave,<br>Suite 300, Mesa, 85201</span></li>
    <li style="top:28px"><span class="icon-disc"><svg><use href="#i-phone"/></svg></span><span>(480) 555-0142</span></li>
    <li style="top:50px"><span class="icon-disc"><svg><use href="#i-mail"/></svg></span><span>sales@bluemoth.agency</span></li>
  </ul>

  <form class="msg-form abs" style="left:258px;top:247px;width:221px;height:169px">
    <p class="msg-form__title" style="left:19px;top:22px">LEAVE US A MESSAGE</p>
    <span class="field" style="left:16px;top:43px;width:91px">Name</span>
    <span class="field" style="left:110px;top:43px;width:91px">Email</span>
    <span class="field" style="left:16px;top:64px;width:91px">Phone</span>
    <span class="field" style="left:110px;top:64px;width:91px">Subject</span>
    <span class="field field--area" style="left:16px;top:84px;width:185px;height:34px">Message</span>
    <span class="btn-outline" style="left:16px;top:128px;width:82px">SEND MESSAGE</span>
  </form>

  <div class="map abs" role="img" aria-label="Street map of the office neighbourhood"></div>
  <svg class="map__pin" viewBox="0 0 24 24" aria-hidden="true"><circle cx="12" cy="12" r="11" fill="#6e1116"/><g transform="translate(6 5) scale(.5)"><use href="#i-pin" fill="#fff"/></g></svg>

  <div class="footer-top">
    <div class="brand"><span class="brand__mark"></span><span class="brand__name">BLUE MOTH</span></div>
    <span class="pill pill--muted">CALL US (480) 555-0142</span>
    <span class="pill pill--brand">GROW YOUR REVENUE</span>
  </div>
  <div class="footer-rule" style="top:713px"></div>

  <div class="footer-col" style="left:62px"><h4>QUICK LINKS</h4><ul><li>About</li><li>Industries</li><li>Training</li><li>Blog</li><li>Services</li><li>Contact</li></ul></div>
  <div class="footer-col" style="left:158px"><h4>SERVICES</h4><ul><li>Programmatic Advertising</li><li>Search Engine Marketing (SEM)</li><li>Search Engine Optimization (SEO)</li><li>Content Marketing</li><li>Email Marketing</li><li>Paid Search Advertising</li><li>Paid Social Advertising</li></ul></div>
  <div class="footer-col" style="left:280px"><h4>INDUSTRIES</h4><ul><li>Ecommerce</li><li>Electricians</li><li>Financial Services Marketing</li><li>Home Builders</li><li>Home Services</li><li>Hvac Companies</li><li>Cosmetic Surgery Centers</li><li>Dental Marketing</li><li>Education</li><li>Healthcare Medical Marketing</li><li>Plumbing Companies</li><li>Podiatrist Marketing</li><li>Landscapers</li></ul></div>
  <div class="footer-col" style="left:390px"><h4>LINKS</h4><ul><li>Training</li><li>Resources</li><li>Privacy Policy</li><li>Sitemap</li><li>Terms Of Use</li><li>Press &amp; Media</li><li>Cookie Policy</li></ul></div>

  <div class="footer-rule" style="top:884px"></div>
  <p class="copyright">© 2024 Company Name | All Rights Reserved</p>
</section>

<!-- ===== Option 2 ===== -->
<section class="page page--two">
  <header class="site-header abs">
    <div class="brand"><span class="brand__mark"></span><span class="brand__name">BLUE MOTH</span></div>
    <ul class="nav abs">
      <li style="left:164px">ABOUT</li>
      <li style="left:204px">INDUSTRIES</li>
      <li style="left:260px">SERVICES</li>
      <li style="left:310px">BLOG</li>
      <li class="is-active" style="left:345px">CONTACT US</li>
    </ul>
    <div class="header-cta abs"><strong>GET A FREE CONSULTATION</strong><span>OR CALL US (480) 555-0142</span></div>
  </header>

  <div class="hero hero--desk abs" role="img" aria-label="Photo of hands typing on a laptop while holding a phone"></div>
  <div class="hero__copy abs">
    <p class="hero__kicker">GET IN TOUCH</p>
    <h2 class="hero__title">CONTACT US</h2>
  </div>

  <form class="msg-form abs" style="left:284px;top:59px;width:182px;height:178px">
    <p class="msg-form__title" style="left:20px;top:17px">LEAVE US A MESSAGE</p>
    <span class="field" style="left:20px;top:34px;width:145px">Name</span>
    <span class="field" style="left:20px;top:55px;width:145px">Email</span>
    <span class="field" style="left:20px;top:76px;width:145px">Phone</span>
    <span class="field field--area" style="left:20px;top:98px;width:145px;height:39px">Message</span>
    <span class="btn-outline" style="left:23px;top:142px;width:72px;height:18px">SEND MESSAGE</span>
  </form>

  <h3 class="section-title abs" style="left:0;top:266px;width:515px;text-align:center">GET IN TOUCH <em>WITH US</em></h3>
  <div class="rule abs" style="left:219px;top:290px;width:76px"></div>
  <style>.page--two .rule::before{margin-left:24px}</style>
  <p class="lead abs" style="left:0;top:306px;width:515px;text-align:center;font-size:7.5px;line-height:9px">Are you ready to kick your business into high gear? Our strategists<br>are standing by. Contact us now!</p>

  <div class="info-card abs" style="left:65px">
    <span class="icon-disc"><svg><use href="#i-pin"/></svg></span>
    <p class="info-card__label">Address</p>
    <p class="info-card__value">18 W. Harbor Ave,<br>Suite 300, Mesa, 85201</p>
  </div>
  <div class="info-card abs" style="left:197px">
    <span class="icon-disc"><svg><use href="#i-phone"/></svg></span>
    <p class="info-card__label">Phone Number</p>
    <p class="info-card__value">(480) 555-0142</p>
  </div>
  <div class="info-card abs" style="left:329px">
    <span class="icon-disc"><svg><use href="#i-mail"/></svg></span>
    <p class="info-card__label">Email address</p>
    <p class="info-card__value">sales@bluemoth.agency</p>
  </div>

  <div class="map abs" role="img" aria-label="Street map of the office neighbourhood"></div>
  <svg class="map__pin" style="left:258px" viewBox="0 0 24 24" aria-hidden="true"><circle cx="12" cy="12" r="11" fill="#6e1116"/><g transform="translate(6 5) scale(.5)"><use href="#i-pin" fill="#fff"/></g></svg>

  <div class="footer-top">
    <div class="brand"><span class="brand__mark"></span><span class="brand__name">BLUE MOTH</span></div>
    <span class="pill pill--muted">CALL US (480) 555-0142</span>
    <span class="pill pill--brand">GROW YOUR REVENUE</span>
  </div>
  <div class="footer-rule" style="top:713px"></div>

  <div class="footer-col" style="left:62px"><h4>QUICK LINKS</h4><ul><li>About</li><li>Industries</li><li>Training</li><li>Blog</li><li>Services</li><li>Contact</li></ul></div>
  <div class="footer-col" style="left:158px"><h4>SERVICES</h4><ul><li>Programmatic Advertising</li><li>Search Engine Marketing (SEM)</li><li>Search Engine Optimization (SEO)</li><li>Content Marketing</li><li>Email Marketing</li><li>Paid Search Advertising</li><li>Paid Social Advertising</li></ul></div>
  <div class="footer-col" style="left:280px"><h4>INDUSTRIES</h4><ul><li>Ecommerce</li><li>Electricians</li><li>Financial Services Marketing</li><li>Home Builders</li><li>Home Services</li><li>Hvac Companies</li><li>Cosmetic Surgery Centers</li><li>Dental Marketing</li><li>Education</li><li>Healthcare Medical Marketing</li><li>Plumbing Companies</li><li>Podiatrist Marketing</li><li>Landscapers</li></ul></div>
  <div class="footer-col" style="left:390px"><h4>LINKS</h4><ul><li>Training</li><li>Resources</li><li>Privacy Policy</li><li>Sitemap</li><li>Terms Of Use</li><li>Press &amp; Media</li><li>Cookie Policy</li></ul></div>

  <div class="footer-rule" style="top:884px"></div>
  <p class="copyright">© 2024 Company Name | All Rights Reserved</p>
</section>

</body>
</html>
```